I would like a new business card designed. I am a kitchen installer for cabinet makers.
I install:
-kitchens
-vanities units
-laundry cabinets
-pantries
-wardrobe shelving
I would like the colors lime green and greys used.
servicing all areas
Also needs to include the words- residential, commercial, industrial
I also want a logo that can be used on work clothes
Modern looking
Target Market(s)
cabinet makers
Industry/Entity Type
Business
Contact Information for Business Card
TR joinery & fitouts pty ltd
0418720946
trjfit@mailbox-example.com.au
www.socialpage-example.com/trjoinery
Logo styles of interest
Emblem Logo
Look and feel

```html
<!DOCTYPE html>
<html lang="en">
<head>
<meta charset="utf-8">
<title>TR joinery &amp; fitouts – business card</title>
<link rel="stylesheet" href="https://fonts.googleapis.com/css2?family=Roboto+Condensed:wght@300;400;700&display=swap">
<style>
  :root {
    --lime: #7cb518;
    --lime-light: #8fc926;
    --lime-dark: #5e9311;
    --white: #ffffff;
    --paper: #fbfbfb;
    --paper-shade: #dcdcdc;
    --grey-text: #5a5a5a;
    --page: #e9e9e9;
  }
  * { box-sizing: border-box; margin: 0; padding: 0; }
  html, body {
    width: 1200px; height: 1024px; overflow: hidden;
    background: var(--page);
    font-family: "Roboto Condensed", Arial, sans-serif;
  }
  .card {
    position: absolute; left: 220px;
    width: 760px; height: 464px;
    overflow: hidden;
    box-shadow: 0 6px 18px rgba(0,0,0,.18);
  }

  /* ---------- contact side ---------- */
  .card-contact {
    top: 32px;
    background: radial-gradient(ellipse at 70% 30%, var(--lime-light), var(--lime) 55%, var(--lime-dark));
    color: var(--white);
  }
  .brand { position: absolute; display: flex; align-items: center; gap: 18px; white-space: nowrap; }
  .brand-mark { flex: none; }
  .brand-name { font-weight: 700; line-height: .95; }
  .brand-name .line-main,
  .brand-name .line-sub { display: block; }

  .card-contact .brand { left: 56px; top: 118px; }
  .card-contact .brand-mark { width: 78px; height: 78px; background: var(--white); border-radius: 10px; }
  .card-contact .brand-name { color: var(--white); }
  .card-contact .line-main { font-size: 54px; }
  .card-contact .line-sub { font-size: 24px; margin-top: 4px; }

  .rule-row {
    position: absolute; left: 0; right: 0; top: 250px;
    display: flex; align-items: center;
  }
  .rule { height: 2px; background: rgba(255,255,255,.85); }
  .rule-long { flex: 1; }
  .rule-short { width: 42px; }
  .holder-name {
    font-weight: 700; font-size: 30px; padding: 0 14px;
    transform: translateY(-18px); white-space: nowrap;
  }
  .divider-v {
    position: absolute; left: 236px; top: 250px; bottom: 0;
    width: 2px; background: rgba(255,255,255,.85);
  }

  .contact-list {
    position: absolute; left: 268px; top: 298px;
    list-style: none; font-weight: 300; font-size: 24px;
  }
  .contact-list li { display: flex; align-items: center; gap: 16px; height: 42px; white-space: nowrap; }
  .contact-icon { width: 20px; height: 20px; flex: none; }
  .contact-icon.square { background: var(--white); border-radius: 3px; width: 18px; height: 18px; margin: 0 1px; }

  /* ---------- services side ---------- */
  .card-services {
    top: 528px;
    background: radial-gradient(ellipse at 45% 40%, var(--white), var(--paper) 45%, var(--paper-shade));
  }
  .card-services .brand { left: 50%; top: 96px; transform: translateX(-50%); }
  .card-services .brand-mark { width: 104px; height: 104px; background: var(--lime); border-radius: 14px; }
  .card-services .brand-name { color: var(--lime); }
  .card-services .line-main { font-size: 72px; }
  .card-services .line-sub { font-size: 30px; margin-top: 6px; }

  .service-list {
    position: absolute; left: 36px; right: 36px; bottom: 66px;
    display: flex; align-items: center; justify-content: space-between;
    list-style: none; color: var(--grey-text);
    font-size: 21px; font-weight: 400;
  }
  .service-list li { display: flex; align-items: center; gap: 12px; white-space: nowrap; }
  .service-list li::before {
    content: ""; width: 3px; height: 22px; background: var(--lime); display: block;
  }
  .service-band {
    position: absolute; left: 0; right: 0; bottom: 0; height: 42px;
    background: var(--lime); color: var(--white);
    display: flex; align-items: center; justify-content: center;
    font-size: 17px; font-weight: 400; letter-spacing: 2px;
    text-transform: uppercase; white-space: nowrap;
  }
  .service-band .sep { margin: 0 12px; }
</style>
</head>
<body>

<section class="card card-contact" aria-label="Business card, contact side">
  <div class="brand">
    <span class="brand-mark"></span>
    <span class="brand-name">
      <span class="line-main">TR joinery</span>
      <span class="line-sub">&amp; fitouts pty ltd</span>
    </span>
  </div>

  <div class="rule-row">
    <span class="rule rule-long"></span>
    <span class="holder-name">Daniel Kovacs</span>
    <span class="rule rule-short"></span>
  </div>
  <span class="divider-v"></span>

  <ul class="contact-list">
    <li>
      <svg class="contact-icon" viewBox="0 0 24 24" aria-hidden="true">
        <path fill="#fff" d="M6.6 10.8a15.1 15.1 0 0 0 6.6 6.6l2.2-2.2a1 1 0 0 1 1-.25 11.4 11.4 0 0 0 3.6.57 1 1 0 0 1 1 1V20a1 1 0 0 1-1 1A17 17 0 0 1 3 4a1 1 0 0 1 1-1h3.5a1 1 0 0 1 1 1c0 1.25.2 2.45.57 3.57a1 1 0 0 1-.25 1z"/>
      </svg>
      0418720946
    </li>
    <li>
      <svg class="contact-icon" viewBox="0 0 24 24" aria-hidden="true">
        <rect x="2" y="5" width="20" height="14" rx="2" fill="#fff"/>
        <path d="M3 6.5l9 6.5 9-6.5" fill="none" stroke="#7cb518" stroke-width="2"/>
      </svg>
      trjfit@mailbox-example.com.au
    </li>
    <li>
      <span class="contact-icon square"></span>
      www.socialpage-example.com/trjoinery
    </li>
  </ul>
</section>

<section class="card card-services" aria-label="Business card, services side">
  <div class="brand">
    <span class="brand-mark"></span>
    <span class="brand-name">
      <span class="line-main">TR joinery</span>
      <span class="line-sub">&amp; fitouts pty ltd</span>
    </span>
  </div>

  <ul class="service-list">
    <li>Kitchens</li>
    <li>Vanities units</li>
    <li>Laundry cabinets</li>
    <li>Pantries</li>
    <li>Wardrobe shelving</li>
  </ul>
  <div class="service-band">
    Residential<span class="sep">•</span>Commercial<span class="sep">•</span>Industrial<span class="sep">—</span>Servicing all areas
  </div>
</section>

</body>
</html>
```